Display board and Flyer Design

We are advertising our business in the local travel centre. We have a package where we get a lightbox (A1 - 594 x 841) and brochure display (either 2 x A4 or 4xDL). We would like to advertise Thornfield Lodge 1852 utilising the design for the gin label attached (minus the gin of course). We would also like to bring attention to the fact that the shop Ashcombe Herbals Co is also at Thornfield Lodge as well as Garden and Gallery and gin tasting. For the brochure we are aiming to advertise everything we do at Thornfield Lodge, we would like the front to be the same as the above for the display board and the back similar to the Ashcombe Herbals brochure that is also attached (essentially so the brochure could sit either way in the display stands. We would then like the internal pages of the brochure to highlight the garden, gallery, giftshop and gin tasting. I have attached another brochure that was designed for our wholesale market. I would like the brochure to have a similar look and feel as the Ashcombe Herbals Co brochure utilising panama and helvetica nue fonts where able Once we have a basic design we can provide some more photography for specific elements i.e. Gin, gallery, giftshop, garden

Font styles to use
Other font styles liked:
• panama/ helvetica

Requirements
Must have
• similar feel to existing ashcombe herbals co brochure
Nice to have
• similar fonts panama/helvetica nue
Should not have
• a design that is nothing like what our brand already is

```html
<!DOCTYPE html>
<html lang="en">
<head>
<meta charset="utf-8">
<title>Thornfield Lodge 1852 – Display Board</title>
<link href="https://fonts.googleapis.com/css2?family=Arimo:wght@400&family=Oswald:wght@600&family=Roboto+Slab:wght@400;800&display=swap" rel="stylesheet">
<style>
  :root {
    --backdrop: #d0d0d0;
    --board: #000000;
    --ink: #ffffff;
    --photo-top: #3b3b3b;
    --photo-mid: #262626;
    --flourish: #2c2c2c;
  }
  html, body {
    margin: 0;
    width: 1200px;
    height: 1200px;
    overflow: hidden;
    background: var(--backdrop);
  }
  .board {
    position: absolute;
    left: 292px;
    top: 166px;
    width: 616px;
    height: 868px;
    background: var(--board);
    overflow: hidden;
    color: var(--ink);
  }
  .hero-photo {
    position: absolute;
    left: 0; top: 0;
    width: 100%;
    height: 536px;
    background: linear-gradient(180deg, var(--photo-top) 0%, var(--photo-mid) 55%, var(--board) 100%);
  }
  .flourish {
    position: absolute;
    width: 78px;
    height: 58px;
    background: var(--flourish);
    border-radius: 4px;
  }
  .flourish--tl { left: 12px; top: 18px; }
  .flourish--tr { left: 520px; top: 18px; }
  .flourish--bl { left: 14px; top: 790px; }
  .flourish--br { left: 520px; top: 790px; }

  .title {
    position: absolute;
    left: 0;
    top: 150px;
    width: 100%;
    margin: 0;
    display: flex;
    flex-direction: column;
    align-items: center;
    text-align: center;
    font-weight: normal;
  }
  .title-name {
    font-family: "Roboto Slab", serif;
    font-weight: 800;
    font-size: 58px;
    line-height: 1.05;
    letter-spacing: 3px;
  }
  .title-rule {
    width: 300px;
    height: 1px;
    background: var(--ink);
    margin: 22px 0 18px;
  }
  .title-year {
    font-family: "Oswald", sans-serif;
    font-weight: 600;
    font-size: 150px;
    line-height: 1;
    letter-spacing: 6px;
  }

  .features {
    position: absolute;
    left: 42px;
    top: 643px;
    display: flex;
    gap: 11px;
  }
  .feature {
    width: 125px;
    height: 125px;
    border: 1px solid var(--ink);
    display: flex;
    flex-direction: column;
    align-items: center;
    justify-content: flex-end;
    box-sizing: border-box;
    padding-bottom: 8px;
  }
  .feature svg { margin-bottom: 8px; }
  .feature-label {
    font-family: "Arimo", Helvetica, sans-serif;
    font-size: 15px;
    letter-spacing: 0.5px;
  }
  .feature--shop {
    justify-content: center;
    padding: 0;
    text-align: center;
    font-family: "Roboto Slab", serif;
    font-weight: 400;
    font-size: 14px;
    line-height: 1.1;
  }
</style>
</head>
<body>
  <main class="board">
    <div class="hero-photo" role="img" aria-label="Dusk photograph of the sandstone Georgian house with its garden, fading to black"></div>

    <div class="flourish flourish--tl" role="img" aria-label="Ornamental corner flourish"></div>
    <div class="flourish flourish--tr" role="img" aria-label="Ornamental corner flourish"></div>
    <div class="flourish flourish--bl" role="img" aria-label="Ornamental corner flourish"></div>
    <div class="flourish flourish--br" role="img" aria-label="Ornamental corner flourish"></div>

    <h1 class="title">
      <span class="title-name">THORNFIELD<br>LODGE</span>
      <span class="title-rule"></span>
      <span class="title-year">1852</span>
    </h1>

    <section class="features">
      <div class="feature feature--shop">ASHCOMBE<br>HERBALS<br>CO.</div>

      <div class="feature">
        <svg width="64" height="64" viewBox="0 0 64 64" fill="none" stroke="#fff" stroke-width="3">
          <g transform="translate(32 32)">
            <ellipse cx="0" cy="-19" rx="6" ry="11"/>
            <ellipse cx="0" cy="-19" rx="6" ry="11" transform="rotate(36)"/>
            <ellipse cx="0" cy="-19" rx="6" ry="11" transform="rotate(72)"/>
            <ellipse cx="0" cy="-19" rx="6" ry="11" transform="rotate(108)"/>
            <ellipse cx="0" cy="-19" rx="6" ry="11" transform="rotate(144)"/>
            <ellipse cx="0" cy="-19" rx="6" ry="11" transform="rotate(180)"/>
            <ellipse cx="0" cy="-19" rx="6" ry="11" transform="rotate(216)"/>
            <ellipse cx="0" cy="-19" rx="6" ry="11" transform="rotate(252)"/>
            <ellipse cx="0" cy="-19" rx="6" ry="11" transform="rotate(288)"/>
            <ellipse cx="0" cy="-19" rx="6" ry="11" transform="rotate(324)"/>
            <circle r="7" fill="#fff"/>
          </g>
        </svg>
        <span class="feature-label">GARDEN</span>
      </div>

      <div class="feature">
        <svg width="92" height="64" viewBox="0 0 92 64" fill="none" stroke="#fff" stroke-width="2.5">
          <rect x="30" y="2" width="36" height="22"/>
          <path d="M2 50 q0 -12 10 -12 q2 -10 26 -10 q24 0 26 10 q10 0 10 12 v8 h-72z" fill="#fff"/>
          <path d="M76 34 h12 l-3 -10 h-6z" fill="#fff"/>
          <line x1="82" y1="34" x2="82" y2="60"/>
          <line x1="77" y1="61" x2="87" y2="61"/>
        </svg>
        <span class="feature-label">GALLERY</span>
      </div>

      <div class="feature">
        <svg width="64" height="66" viewBox="0 0 64 66" fill="none" stroke="#fff" stroke-width="2.5">
          <path d="M12 2 h8 v16 q6 6 6 16 v30 h-20 v-30 q0 -10 6 -16z"/>
          <path d="M40 2 h8 v16 q6 6 6 16 v30 h-20 v-30 q0 -10 6 -16z"/>
        </svg>
        <span class="feature-label">GIN TASTING</span>
      </div>
    </section>
  </main>
</body>
</html>
```